author needs a Book Cover design

Needs a book cover design that matches the title in some way.
Book Title is- 9 Lanterns Beyond the Quiet Harbor at Dusk.
Subtile- Gentle Lessons On Morning Gardens.
Author Name:-Gordon Peltiway, Sr.

Final Design is subject to Book Publisher's requirement.

Font styles to use
Serif

Requirements
Must have
• Follow these recommended specifications for your cover file:
• Page Size: Your cover should be a single (one-piece) PDF that includes the back cover, spine, and front cover. You can submit your cover on any size page as long as the printable area is measured exactly for your book's trim size, spine width, and allows at least .125” bleed, centered horizontally and vertically.
• Minimum Cover Width: Bleed + Back Cover Trim Size + Spine Width + Front Cover Trim Size + Bleed
• Minimum Cover Height: Bleed + Book Height Trim Size + Bleed
• Trim Size: Your cover should be the same trim size as you choose in the Title Information when setting up your book. For example, submitting a cover that was previously used for a 6.25” x 9.25” book would not work for a 6” x 9” book.
• Barcodes: For manufacturing and distribution reasons, your book's back cover must include a valid ISBN barcode. If your cover already has an ISBN barcode, make sure it is high-resolution, or at least 300 dpi, and 1.5" - 2" in width with proportional height. Ideally, this barcode should be 2” wide by 1.2” tall. Also, check to make sure you have the rights to use the ISBN on your cover, because not all services allow you to use their ISBNs elsewhere.
• QR codes: There are no set size restrictions, but the quality (resolution) of the image must be set to at least 300 dpi. Make sure you have the rights to use the code.
• If your artwork does not include a barcode, we will automatically add one in the lower right-hand corner of your book's back cover, free of charge. Our system will place the ISBN barcode in a space 2" wide and 1.2" tall. The bottom of this barcode is located 1/4" up from the bottom trim line of the cover. The right side of the barcode is located 1/4" to the left of the spine. Please ensure that you don't have any important images or text in the barcode location. You can also refer to our Artwork Templates for the exact size and position of the ISBN barcode on your final cover.
• If you don’t have an ISBN already on your cover, but you have live graphic or text elements in the location that our system will place the ISBN, you will need to move those elements or place the ISBN in a different location yourself.
• Publishing Logos: We do not add our logo to your book.
• Spine Width and Variance: If your artwork was created for a different service, please make sure that the spine width of your current cover matches our spine width. Different services may use different paper thickness, which is why the spine width of your cover artwork could be correct for another service but incorrect for our service.
• Ideally, you should avoid hard vertical lines separating your front or back cover panels from your spine and should allow for at least a .125" variance of your spine on each side (for example, the text on a 1" spine should be no larger than .75" wide). For books with a page count of less than 130 pages, we strongly recommend a blank spine.
• Your spine width should be calculated based on the number of pages in your book and using the appropriate formula:
• Black and White Interior Book Spine Width:
• White paper: Number of pages x .002252 = Spine width in inches
• Cream paper: Number of pages x .0025 = Spine width in inches
• Color Interior Book Spine Width:
• Number of pages x .002347 = Spine width in inches
• Example of spine width calculation for a 120-page black and white interior book with white paper:
• 120 x .002252 = .27" spine width
• Text and Image Placement: All live cover elements, or text and images that cannot be cut, must be at least .125" inside the trim lines to ensure no important elements are cut during the bookmaking process and the appearance of your printed books is consistent.
• Bleed: Your cover's background must extend at least .125" beyond the final trim line to accommodate for cutting/trimming tolerance.
• Crop/Registration Marks: Please do not include any crop or registration marks on your files, as they may interfere with the binding process or appear on the cover. We use our own measurements, specific to our systems, for cutting and binding; crop or registration marks placed by you could interfere with this process.
• Images and Fonts: Any images you include on your book's cover may be tagged with your choice of CMYK or RGB profiles or left untagged in a generic color space. All images should be sized at 100%, flattened to one layer and placed in your native document at a resolution of at least 300 DPI. You should also embed all fonts in your PDF file.
• Gordon, I hope this information is helpful to you. Please feel free to contact us if you have any other questions or concerns.
• Best regards,
• *WILL SUPPLY THE PAGE NUMBERS INFORMATION
• Lenora
• PrintHollow Member Services
Nice to have
• An attractive design that matches the title. Design can include backgrounds

```html
<!DOCTYPE html>
<html lang="en">
<head>
<meta charset="utf-8">
<title>9 Lanterns Beyond the Quiet Harbor at Dusk — Book Cover</title>
<link href="https://fonts.googleapis.com/css2?family=Cinzel:wght@400;700&family=Oswald:wght@500;700&display=swap" rel="stylesheet">
<style>
  :root {
    --stage: #e4e4e4;
    --paper: #f4f4f4;
    --ink: #222222;
    --slate: #505552;
    --ember: #c9401e;
    --stone-light: #d9d9d9;
    --stone-dark: #7a7a7a;
  }
  html, body {
    margin: 0;
    padding: 0;
    width: 1200px;
    height: 1059px;
    overflow: hidden;
    background: var(--stage);
  }
  .cover {
    position: absolute;
    left: 280px;
    top: 50px;
    width: 640px;
    height: 960px;
    background: var(--paper);
    box-shadow: 0 6px 24px rgba(0,0,0,0.18);
    overflow: hidden;
  }
  .title { margin: 0; }
  .author {
    position: absolute;
    top: 38px;
    left: 0;
    width: 100%;
    text-align: center;
    font-family: "Cinzel", serif;
    font-weight: 400;
    font-size: 40px;
    letter-spacing: 1px;
    color: var(--ink);
  }
  .title-top {
    position: absolute;
    top: 100px;
    left: 30px;
    right: 30px;
    display: flex;
    align-items: flex-end;
    justify-content: center;
    font-family: "Oswald", sans-serif;
    font-weight: 700;
    color: var(--slate);
    line-height: 1;
  }
  .title-number {
    font-size: 150px;
    margin-right: 12px;
  }
  .title-word {
    font-size: 96px;
    letter-spacing: -1px;
    padding-bottom: 6px;
  }
  .title-link {
    position: absolute;
    top: 258px;
    left: 0;
    width: 100%;
    text-align: center;
    font-family: "Oswald", sans-serif;
    font-weight: 500;
    font-size: 40px;
    line-height: 1.2;
    color: var(--slate);
    letter-spacing: 1px;
  }
  .title-key {
    position: absolute;
    top: 322px;
    left: 0;
    width: 100%;
    text-align: center;
    font-family: "Cinzel", serif;
    font-weight: 700;
    font-size: 118px;
    line-height: 1;
    color: var(--ember);
    letter-spacing: 2px;
  }
  .title-tail {
    position: absolute;
    top: 478px;
    left: 0;
    width: 100%;
    text-align: center;
    font-family: "Oswald", sans-serif;
    font-weight: 700;
    font-size: 44px;
    line-height: 1.2;
    color: var(--slate);
    letter-spacing: 1px;
  }
  .artwork {
    position: absolute;
    left: 20px;
    right: 20px;
    top: 560px;
    height: 320px;
  }
  .artwork svg { display: block; width: 100%; height: 100%; }
  .subtitle {
    position: absolute;
    bottom: 26px;
    left: 0;
    width: 100%;
    text-align: center;
    font-family: "Oswald", sans-serif;
    font-weight: 700;
    font-size: 30px;
    letter-spacing: 1px;
    color: var(--ink);
  }
  .subtitle .accent { color: var(--ember); }
</style>
</head>
<body>
  <main class="cover">
    <div class="author">Gordon Peltiway, Sr</div>

    <h1 class="title">
      <span class="title-top">
        <span class="title-number">9</span>
        <span class="title-word">LANTERNS</span>
      </span>
      <span class="title-link">BEYOND THE</span>
      <span class="title-key">QUIET</span>
      <span class="title-tail">HARBOR AT DUSK</span>
    </h1>

    <div class="artwork">
      <svg role="img" aria-label="Black and white illustration of a carved stone figure, crouching, the cover's central artwork" viewBox="0 0 600 320" preserveAspectRatio="none">
        <defs>
          <radialGradient id="stone" cx="50%" cy="45%" r="60%">
            <stop offset="0%" stop-color="#d9d9d9"/>
            <stop offset="70%" stop-color="#7a7a7a"/>
            <stop offset="100%" stop-color="#f4f4f4"/>
          </radialGradient>
        </defs>
        <rect x="0" y="0" width="600" height="320" fill="url(#stone)"/>
      </svg>
    </div>

    <div class="subtitle">
      GENTLE <span class="accent">LESSONS</span> ON <span class="accent">MORNING GARDENS</span>
    </div>
  </main>
</body>
</html>
```